Classy, Elegant, Simple Business Card Design

Looking to have a classy, simple, and elegant design. Want a top notch designed business card. I really like the look of the new brivo credit card. I also like the design I attached. I am trying to reach 21-29 year old females for booking us for there wedding or event. We offer Disc Jockey Service, Photo Booth Rentals, and Uplighting .

Target Market(s)

21-28 year old females

Contact Information for Business Card

Has to have logo, website, email, and phone number

Font styles to use
Other font styles liked:
• open to font choice, modern, clean
Designer to choose
33a6d7
0791cd
0555a3
ffffff

Requirements
Must have
• Has to have logo, website, email, and phone number
Nice to have
• I really like the design of the new brivo credit card. I also included my logo and some designs I like
Should not have
• clutter or too much info

```html
<!DOCTYPE html>
<html lang="en">
<head>
<meta charset="utf-8">
<title>Tidewell Event Group – Business Card</title>
<link rel="stylesheet" href="https://fonts.googleapis.com/css2?family=Open+Sans:wght@400;600&display=swap">
<style>
  :root {
    --ink: #000000;
    --paper: #ffffff;
    --blue-front: #1a6dbb;
    --blue-edge: #0b3a70;
    --blue-logo: #0791cd;
    --blue-band: #33a6d7;
    --backdrop-top: #b9bbbe;
    --backdrop-bottom: #dfe1e3;
  }
  * { margin: 0; padding: 0; box-sizing: border-box; }
  html, body { width: 1200px; height: 873px; overflow: hidden; }
  body {
    background: linear-gradient(180deg, var(--backdrop-top), var(--backdrop-bottom));
    font-family: "Open Sans", Arial, sans-serif;
    position: relative;
  }
  .card {
    position: absolute;
    top: 282px;
    width: 540px;
    height: 309px;
    background: var(--ink);
    overflow: hidden;
    box-shadow: 0 14px 30px rgba(0,0,0,0.28);
  }
  .card--front { left: 40px; }
  .card--back { left: 620px; }

  .card__panel { position: absolute; inset: 0; width: 100%; height: 100%; }

  .brand {
    position: absolute;
    display: flex;
    align-items: center;
    gap: 10px;
    color: var(--blue-logo);
    font-weight: 600;
    text-transform: uppercase;
    white-space: nowrap;
  }
  .brand__dot {
    width: 14px; height: 14px;
    border-radius: 50%;
    background: var(--blue-logo);
    flex: none;
  }
  .card--front .brand {
    top: 42px; right: 34px;
    font-size: 17px;
    letter-spacing: 3px;
  }
  .card--back .brand {
    top: 50%; left: 50%;
    transform: translate(-50%, -60%);
    font-size: 22px;
    letter-spacing: 4px;
  }
  .brand__name { line-height: 1.35; }

  .contact {
    position: absolute;
    left: 110px;
    top: 186px;
    list-style: none;
    color: var(--paper);
    font-size: 14px;
    font-weight: 600;
    line-height: 1.75;
  }
  .contact__label { display: inline-block; width: 26px; }

  .card__band {
    position: absolute;
    left: 0; right: 0; bottom: 0;
    height: 24px;
    background: var(--blue-band);
  }
</style>
</head>
<body>

  <section class="card card--front" aria-label="Business card, front">
    <svg class="card__panel" viewBox="0 0 540 309" preserveAspectRatio="none" aria-hidden="true">
      <polygon points="0,108 428,160 406,309 0,309" fill="var(--blue-edge)"/>
      <polygon points="0,118 418,166 398,309 0,309" fill="var(--blue-front)"/>
    </svg>
    <div class="brand">
      <span class="brand__dot"></span>
      <span class="brand__name">Tidewell Event Group</span>
    </div>
    <ul class="contact">
      <li><span class="contact__label">m:</span>+1 555 014 2290</li>
      <li><span class="contact__label">e:</span>info@tidewellevents.com</li>
      <li><span class="contact__label">w:</span>www.tidewellevents.com</li>
    </ul>
  </section>

  <section class="card card--back" aria-label="Business card, back">
    <div class="brand">
      <span class="brand__dot"></span>
      <span class="brand__name">Tidewell Event Group</span>
    </div>
    <div class="card__band"></div>
  </section>

</body>
</html>
```